Webdesign für Software Ingenieurbüro
Vielen Dank für das professionelle Design, Umsetzung mit WordPress und rasche Reaktionszeiten. MondscheinKobold geht die Extrameile.
Zielgruppe
English text below
Meine Firma erstellt Software und bietet sämtliche Dienstleistungen rund um die Softwareentwicklung an.
Die Zielgruppe sind Auftraggeber, welche Software-Engineering/Entwicklungsaufträge vergeben.
English
My company creates software and offers all services related to software development.
The target group are those who award software engineering / development contracts.
Aufgabenstellung
Die bestehende Seite www.tarnvok-systems.ch soll neu und modern designed werden. Die Struktur der Seite (Menuunterteilung) kann (muss aber nicht zwingend) übernommen werden.
Das Logo kann, muss aber nicht übernommen werden.
Ev. als OnePage-Seite gestalten.
Responsive-Design ist zwingend, d.h. die Seite muss sowohl auf dem Desktop wie auch auf dem Mobile-Gerät ansprechend aussehen.
Zur Illustration soll auf Fotos verzichtet werden. Aber es können sehr gerne Vektorgrafiken für die Illustration und/oder Icons verwendet werden.
Link auf Social-Media Qorvu muss vorhanden sein.
Der persönliche Kontakt zum Kunden ist mir wichtig, deshalb sollte mein Foto vorhanden sein. Ev. nicht so prominent wie auf der aktuellen Seite.
Die Umsetzung wird mit Wordpress und einem Standard-Theme geschehen. Falls Sie Wordpress kennen, können Sie das Theme angeben, mit welchem sich die Seite umsetzen lässt.
The existing site www.tarnvok-systems.ch is to be redesigned and modernized. The structure of the page (menu subdivision) can (but does not have to be) mandatory.
The logo can, but does not have to be adopted.
Ev. as a OnePage page.
Responsive design is required, the page must look appealing both on the desktop and on the mobile device.
For the illustration, photographs are not desired. But vector graphics can be used for illustration and / or icons.
Link to social media Qorvu must be available.
Personal contact with the customer is important to me, so my photo should be available. Ev. not as prominent as on the current page.
The implementation will be done with Wordpress and a standard theme. If you are familiar with Wordpress, you can specify the theme with which the page can be implemented.

```html
<!DOCTYPE html>
<html lang="de">
<head>
<meta charset="utf-8">
<title>Tarnvok Systems GmbH – Softwareentwicklung</title>
<link rel="stylesheet" href="https://fonts.googleapis.com/css2?family=Lato:wght@300;400&family=Raleway:wght@400;500;600;700&display=swap">
<style>
  :root {
    --ink: #22303c;
    --nav: #3d5466;
    --header-bg: #ffffff;
    --hero-light: #e4ecee;
    --hero-mid: #c9d6da;
    --hero-dark: #a9bcc2;
    --title: #2f3a42;
    --copy: #3e4a52;
    --btn-start: #1f5a7a;
    --btn-end: #2f8fbf;
    --btn-text: #f6e37a;
    --rule: #dfe5e8;
  }
  * { box-sizing: border-box; margin: 0; padding: 0; }
  html, body { width: 1200px; height: 600px; overflow: hidden; }
  body { font-family: "Raleway", sans-serif; background: var(--header-bg); }

  .site { width: 1200px; height: 600px; display: flex; flex-direction: column; }

  .site-header {
    height: 120px;
    display: flex; align-items: center; justify-content: space-between;
    padding: 0 170px 0 180px;
    border-bottom: 1px solid var(--rule);
    background: var(--header-bg);
  }
  .brand { display: flex; align-items: center; gap: 12px; }
  .brand-mark { width: 26px; height: 26px; background: var(--btn-end); }
  .brand-name { font-weight: 600; font-size: 25px; color: var(--ink); letter-spacing: 0.2px; }

  .main-nav { display: flex; gap: 22px; }
  .main-nav a {
    font-weight: 600; font-size: 14px; color: var(--nav);
    text-decoration: none; letter-spacing: 0.4px;
  }

  .hero { position: relative; flex: 1; overflow: hidden; }
  .hero-backdrop {
    position: absolute; inset: 0;
    background: radial-gradient(ellipse at 50% 40%, var(--hero-light) 0%, var(--hero-mid) 60%, var(--hero-dark) 100%);
  }
  .hero-content {
    position: relative; text-align: center; padding-top: 108px;
  }
  .hero-title {
    font-family: "Lato", sans-serif; font-weight: 300;
    font-size: 34px; color: var(--title); letter-spacing: 0.3px;
  }
  .hero-lead {
    margin: 28px auto 0; width: 560px;
    font-size: 13px; line-height: 24px; color: var(--copy);
  }
  .hero-actions { margin-top: 34px; display: flex; justify-content: center; gap: 12px; }
  .btn {
    display: inline-block; padding: 0 14px; height: 34px; line-height: 34px;
    border-radius: 17px; font-weight: 500; font-size: 15px;
    color: var(--btn-text); text-decoration: none;
    background: linear-gradient(90deg, var(--btn-start), var(--btn-end));
  }
  .scroll-hint { position: absolute; left: 50%; bottom: 14px; transform: translateX(-50%); }
</style>
</head>
<body>
<div class="site">
  <header class="site-header">
    <div class="brand">
      <span class="brand-mark"></span>
      <span class="brand-name">Tarnvok Systems GmbH</span>
    </div>
    <nav class="main-nav">
      <a href="#start">Start</a>
      <a href="#profil">Profil</a>
      <a href="#dienstleistungen">Dienstleistungen</a>
      <a href="#methoden">Methoden</a>
      <a href="#referenzen">Referenzen</a>
      <a href="#kontakt">Kontakt</a>
    </nav>
  </header>

  <section class="hero" id="start">
    <div class="hero-backdrop" role="img" aria-label="Hintergrundbild: abstrakte helle Lichtfasern in Blaugrau"></div>
    <div class="hero-content">
      <h1 class="hero-title">Softwareentwicklung, modern &amp; agil</h1>
      <p class="hero-lead">Tarnvok Systems mit Sitz in Seewil fokussiert sich auf professionelle Softwareentwicklung unter Verwendung modernster Technologien und leichtgewichtiger Prozesse</p>
      <div class="hero-actions">
        <a class="btn" href="#dienstleistungen">Dienstleistungen</a>
        <a class="btn" href="#kontakt">Kontakt aufnehmen</a>
      </div>
    </div>
    <svg class="scroll-hint" width="30" height="30" viewBox="0 0 30 30" aria-label="Nach unten scrollen">
      <circle cx="15" cy="15" r="13" fill="none" stroke="#3d5466" stroke-width="1.6"/>
      <polyline points="9,12 15,18 21,12" fill="none" stroke="#3d5466" stroke-width="1.8" stroke-linecap="round" stroke-linejoin="round"/>
    </svg>
  </section>
</div>
</body>
</html>
```